We provide Professional DJ Service in different genres of music ranging from Latin to Hip/Hop R&B/TOP 40 etc...we also help promote DJ/Music/Artists events Internationally. I am looking for the main color of my business to be fluorescent lime green with some traces of 'smurf' blue. Maybe military feel attached to it as well as I am active duty military and all of my DJ's are either active or retired. That would be our main focus. We can do anything from Formal military balls to backyard parties We are also mobile and can be hired by local clubs/pubs/bars.

Target Market(s)

Military Community/Events/ Local nightclubs/pubs/bars looking to hire professional DJ's.

Industry/Entity Type

Entertainment

Contact Information for Business Card

Brevane Entertainment (Professional DJ Service/Event Promoter)/email:dorkabrevane@quelmail.example/ Plazzly logo with address or scan directly to my page. (Plazzly-search Brevane Entertainment) Tomas 'DJ Kestrel' Brevane. Owner/DJ/Promoter

Font styles to use
Serif

Colors
acd136
33a6d7

Requirements
Must have
• Looking for on back of card Plazzly logo and scanbar leading directly to my PZ page...if not possible then Plazzly.com search Brevane Entertainment (or both).
Nice to have
• The attachment that I sent has my logo that I would like to use, however it is not a finished product. Is this only for business cards layout or also to spruce up or make my logo better? It's the Brevane

```html
<!DOCTYPE html>
<html lang="en">
<head>
<meta charset="utf-8">
<title>Brevane Entertainment – Business Card</title>
<link rel="stylesheet" href="https://fonts.googleapis.com/css2?family=Exo+2:wght@400;600;700&display=swap">
<style>
  :root {
    --page-bg: #e9e6e1;
    --card-black: #050607;
    --brand-blue: #33a6d7;
    --sky-blue: #3fc2e8;
    --deep-blue: #1d8fc4;
    --lime: #acd136;
    --white: #ffffff;
    --soft-white: #e6edf0;
  }
  html, body {
    margin: 0;
    width: 1200px;
    height: 1023px;
    overflow: hidden;
    background: var(--page-bg);
    font-family: "Exo 2", sans-serif;
  }
  .sheet {
    position: relative;
    width: 1200px;
    height: 1023px;
  }
  .card {
    position: absolute;
    left: 240px;
    width: 720px;
    height: 411px;
    border-radius: 6px;
    overflow: hidden;
    box-shadow: 0 10px 28px rgba(0,0,0,0.25);
  }

  /* ---------- Front ---------- */
  .card-front {
    top: 64px;
    background: var(--card-black);
  }
  .crowd-art {
    position: absolute;
    left: 250px;
    top: 150px;
    width: 470px;
    height: 261px;
    background: linear-gradient(180deg, rgba(63,194,232,0) 0%, var(--sky-blue) 38%, var(--brand-blue) 100%);
    clip-path: polygon(0 88%, 8% 60%, 16% 70%, 24% 40%, 34% 50%, 44% 22%, 55% 32%, 66% 10%, 78% 18%, 90% 0, 100% 6%, 100% 100%, 0 100%);
  }
  .front-heading {
    position: absolute;
    right: 40px;
    top: 34px;
    text-align: right;
  }
  .owner-name {
    margin: 0;
    color: var(--sky-blue);
    font-size: 31px;
    font-weight: 700;
    letter-spacing: 0.3px;
  }
  .owner-role, .owner-email {
    margin: 6px 0 0;
    color: var(--soft-white);
    font-size: 17px;
    font-weight: 400;
  }
  .brand-badge {
    position: absolute;
    left: 52px;
    top: 190px;
    width: 170px;
    height: 170px;
    border-radius: 50%;
    background: var(--lime);
    display: flex;
    align-items: center;
    justify-content: center;
    text-align: center;
  }
  .brand-badge span {
    color: var(--card-black);
    font-size: 20px;
    font-weight: 700;
    line-height: 1.15;
  }
  .tagline {
    position: absolute;
    right: 34px;
    bottom: 26px;
    margin: 0;
    color: var(--white);
    font-size: 21px;
    font-weight: 600;
    letter-spacing: 0.6px;
  }

  /* ---------- Back ---------- */
  .card-back {
    top: 548px;
    background: radial-gradient(circle at 60% 45%, var(--sky-blue) 0%, var(--brand-blue) 55%, var(--deep-blue) 100%);
  }
  .back-badge {
    position: absolute;
    left: 385px;
    top: 70px;
    width: 200px;
    height: 200px;
    border-radius: 50%;
    background: var(--white);
    display: flex;
    align-items: center;
    justify-content: center;
    text-align: center;
  }
  .back-badge span {
    color: var(--brand-blue);
    font-size: 24px;
    font-weight: 700;
    line-height: 1.15;
  }
  .search-line {
    position: absolute;
    left: 40px;
    right: 40px;
    bottom: 36px;
    display: flex;
    align-items: center;
    gap: 14px;
    color: var(--white);
  }
  .network-mark {
    width: 30px;
    height: 30px;
    border-radius: 5px;
    background: var(--white);
  }
  .search-text {
    font-size: 24px;
    font-weight: 600;
    letter-spacing: 1px;
  }
  .search-icon { margin-left: 4px; }
</style>
</head>
<body>
<main class="sheet">

  <section class="card card-front" aria-label="Business card front">
    <div class="crowd-art" role="img" aria-label="Silhouette of a cheering party crowd with raised hands"></div>
    <header class="front-heading">
      <h1 class="owner-name">Tomas 'DJ Kestrel' Brevane</h1>
      <p class="owner-role">Owner | Dj | Promoter</p>
      <p class="owner-email">dorkabrevane@quelmail.example</p>
    </header>
    <div class="brand-badge"><span>Brevane<br>Entertainment</span></div>
    <p class="tagline">Professional DJ Service · Event Promoter</p>
  </section>

  <section class="card card-back" aria-label="Business card back">
    <div class="back-badge"><span>Brevane<br>Entertainment</span></div>
    <div class="search-line">
      <span class="network-mark" aria-label="Plazzly"></span>
      <span class="search-text">/ Brevane Entertainment /</span>
      <svg class="search-icon" width="30" height="30" viewBox="0 0 30 30" aria-label="Search">
        <circle cx="18" cy="12" r="8" fill="none" stroke="#ffffff" stroke-width="3"/>
        <line x1="12" y1="18" x2="4" y2="26" stroke="#ffffff" stroke-width="3" stroke-linecap="round"/>
      </svg>
    </div>
  </section>

</main>
</body>
</html>
```